Young Architect Bussiness Card

English is not my first language (spanish is).
Need a bussiness card design for my best friend who is about to graduate from college, Licentiate degree in architecture, so she needs business cards to start networking, currently she has no porfolio, web page or facebook. so she is relying on her cel phone and gmail, but should leave space for one of them (facebook)

Design for business card should be modern, maybe something with construction blue prints patern or 3D modelling.

Name: Mariela Fonseca Arrieta
Licentiate in Arquitecture
Cel: (506) XXX-4827
email: marielaXXX@correovela.com

Services, although im not sure if it has to be there or not:
Anteproyectos / Proposal design
Inspecciones / Site Inspections
Modelado 3D / 3D modelling
Planos Constructivos / Construction Blue Prints
Presupuestos / Budgets

Design should be in spanish

Contact Information for Business Card

Name: Mariela Fonseca, Arquitecto
Associtation code : XXXX
Phone: (506) XXXX-XXXX
Email: xxx@correovela.com
Facebook: xxxx

Requirements
Must have
• Design for business card should be modern, maybe something with construction blue prints patern or 3D modelling.
Nice to have
• Something like a transition from 2D to 3D.

```html
<!DOCTYPE html>
<html lang="es">
<head>
<meta charset="UTF-8">
<title>Arq. Mariela Fonseca — Tarjeta de presentación</title>
<link href="https://fonts.googleapis.com/css2?family=Source+Code+Pro:wght@300;400;700;900&display=swap" rel="stylesheet">
<style>
  :root {
    --page: #e9e7e2;
    --yellow: #f2bd2c;
    --black: #0d0d0d;
    --charcoal: #262626;
    --white: #ffffff;
    --ink: #1a1a1a;
    --paper-light: #f1f1ef;
    --paper-mid: #d9dadb;
  }
  * { margin: 0; padding: 0; box-sizing: border-box; }
  html, body { width: 1200px; height: 900px; overflow: hidden; }
  body {
    background: var(--page);
    font-family: "Source Code Pro", monospace;
    position: relative;
  }
  .card {
    position: absolute;
    left: 250px;
    width: 700px;
    height: 400px;
    overflow: hidden;
    box-shadow: 0 6px 18px rgba(0,0,0,.18);
  }
  .card--front { top: 40px; background: var(--yellow); }
  .card--back { top: 470px; }
  .card svg.shape { position: absolute; inset: 0; width: 100%; height: 100%; }

  .name {
    position: absolute;
    white-space: nowrap;
    letter-spacing: 1px;
  }
  .name__title { font-weight: 300; }
  .name__first { font-weight: 900; }
  .name__last { font-weight: 300; }
  .contact { position: absolute; white-space: nowrap; font-weight: 300; letter-spacing: 1px; }

  /* front */
  .card--front .name { left: 40px; top: 62px; font-size: 46px; color: var(--ink); }
  .card--front .contact { left: 44px; top: 128px; font-size: 22px; color: var(--ink); }
  .service {
    position: absolute;
    font-weight: 900;
    font-size: 20px;
    line-height: 1;
    letter-spacing: 0.5px;
    white-space: nowrap;
  }
  .service--white { color: var(--white); }
  .service--yellow { color: var(--yellow); }
  .service--modelado { left: 520px; top: 198px; }
  .service--inspecciones { left: 395px; top: 240px; }
  .service--planos { left: 410px; top: 282px; }
  .service--anteproyectos { left: 40px; top: 325px; }
  .service--presupuestos { left: 218px; top: 360px; }

  /* back */
  .illustration {
    position: absolute; inset: 0;
    background: linear-gradient(160deg, var(--paper-light) 0%, var(--paper-mid) 60%, #c9c9c6 100%);
  }
  .card--back .name { right: 36px; top: 258px; font-size: 44px; color: var(--white); }
  .card--back .name__title { color: var(--yellow); }
  .card--back .contact { right: 40px; top: 322px; font-size: 21px; color: var(--white); }
</style>
</head>
<body>

<section class="card card--front" aria-label="Frente de la tarjeta">
  <svg class="shape" viewBox="0 0 700 400" aria-hidden="true">
    <polygon points="0,290 370,245 370,215 700,160 700,400 0,400" fill="var(--black)"/>
  </svg>
  <p class="name"><span class="name__title">Arq.</span><span class="name__first">MARIELA</span><span class="name__last">FONSECA</span></p>
  <p class="contact">(506)XXXX-XXXX | xxx@correovela.com</p>

  <span class="service service--white service--modelado">Modelado 3D</span>
  <span class="service service--yellow service--inspecciones">Inspecciones</span>
  <span class="service service--white service--planos">Planos Constructivos</span>
  <span class="service service--white service--anteproyectos">Anteproyectos</span>
  <span class="service service--yellow service--presupuestos">Presupuestos</span>
</section>

<section class="card card--back" aria-label="Reverso de la tarjeta">
  <div class="illustration" role="img" aria-label="Ilustración de planos arquitectónicos con manos, escuadra, nivel, lápices y transportador sobre el escritorio"></div>
  <svg class="shape" viewBox="0 0 700 400" aria-hidden="true">
    <polygon points="0,400 0,350 700,130 700,400" fill="var(--charcoal)" fill-opacity="0.94"/>
  </svg>
  <p class="name"><span class="name__title">Arq. </span><span class="name__first">MARIELA</span> <span class="name__last">FONSECA</span></p>
  <p class="contact">(506)XXXX-XXXX | xxx@correovela.com</p>
</section>

</body>
</html>
```